Business Card Design Project for Investment Fund

Orvanel Asset Partners is an emerging wealth management firm based in New Jersey. It offers superior investment returns to high net worth individuals and institutions by finding undervalued assets.
We recently selected a company logo which was inspired by the Tucana constellation. Beta Tucanae is a group of six stars, containing star cluster 47 Tucanae, rated the second brightest object in the sky.
Now we need a business card design. Since we are an investment firm, the design should project a sense of stability, growth and professionalism. The owner is interested in something simple yet striking, which of course is consistent with the logo.
Target Market(s)
Wealthy individuals, probably middle aged or older, in the US
Industry/Entity Type
Investment

```html
<!DOCTYPE html>
<html lang="en">
<head>
<meta charset="utf-8">
<title>Orvanel Asset Partners – Business Card</title>
<link rel="stylesheet" href="https://fonts.googleapis.com/css2?family=Ubuntu:wght@400;500;700&display=swap">
<style>
  :root {
    --backdrop: #262626;
    --card: #f7f7f7;
    --ink: #2f2f2f;
    --ink-soft: #555555;
    --brand-blue: #2c2a86;
    --brand-blue-deep: #1c1a5c;
    --accent-bar: #333333;
    --rule: #c9c9c9;
    --grey-name: #4a4a4a;
  }
  * { margin: 0; padding: 0; box-sizing: border-box; }
  html, body {
    width: 1200px; height: 900px; overflow: hidden;
    background: var(--backdrop);
    font-family: "Ubuntu", sans-serif;
  }
  .stage { position: relative; width: 1200px; height: 900px; }

  .card {
    position: absolute;
    width: 600px; height: 343px;
    background: var(--card);
    box-shadow: 0 14px 40px rgba(0,0,0,.55);
  }
  .card--front { left: 50px; top: 60px; }
  .card--back { left: 550px; top: 490px; }

  /* brand block: plain square + name */
  .brand { position: absolute; display: flex; align-items: center; gap: 18px; }
  .brand__square {
    width: 86px; height: 86px; border-radius: 12px;
    background: linear-gradient(160deg, var(--brand-blue), var(--brand-blue-deep));
    flex: none;
  }
  .brand__name {
    color: var(--grey-name);
    font-weight: 500;
    font-size: 34px;
    line-height: 1.05;
    letter-spacing: .5px;
  }
  .card--front .brand { left: 50%; top: 50%; transform: translate(-50%, -50%); }

  .card--back .brand { left: 40px; bottom: 36px; gap: 14px; }
  .card--back .brand__square { width: 64px; height: 64px; border-radius: 9px; }
  .card--back .brand__name { font-size: 24px; }

  .accent-bar {
    position: absolute; left: 40px; top: 0;
    width: 44px; height: 118px;
    background: var(--accent-bar);
  }

  .holder { position: absolute; right: 30px; top: 22px; text-align: right; }
  .holder__name { font-size: 22px; font-weight: 700; color: var(--ink); }
  .holder__surname { color: var(--brand-blue); }
  .holder__role { font-size: 11px; color: var(--ink-soft); letter-spacing: .5px; }

  .contact { position: absolute; right: 30px; left: 220px; top: 88px; }
  .contact__row {
    display: flex; justify-content: flex-end; align-items: center; gap: 12px;
    font-size: 14px; color: var(--ink); line-height: 22px;
  }
  .contact__row svg { width: 14px; height: 14px; flex: none; fill: var(--ink-soft); }
  .contact__rule { height: 1px; background: var(--rule); margin: 10px 0 10px 0; }
  .contact__address { font-size: 15px; text-align: right; line-height: 20px; }
</style>
</head>
<body>
<main class="stage">

  <section class="card card--front" aria-label="Card front">
    <div class="brand">
      <span class="brand__square"></span>
      <span class="brand__name">Orvanel<br>Asset Partners</span>
    </div>
  </section>

  <section class="card card--back" aria-label="Card back">
    <div class="accent-bar"></div>

    <header class="holder">
      <div class="holder__name">Daniel <span class="holder__surname">Harker</span></div>
      <div class="holder__role">CEO</div>
    </header>

    <div class="contact">
      <div class="contact__row">212 555 0147
        <svg viewBox="0 0 14 14"><rect x="3" y="1" width="8" height="12" rx="1.5" fill="none" stroke="#555" stroke-width="1.4"/></svg>
      </div>
      <div class="contact__row">dharker@orvanelasset.com
        <svg viewBox="0 0 14 14"><rect x="1" y="3" width="12" height="8" fill="#555"/><path d="M1 3 L7 8 L13 3" fill="none" stroke="#f7f7f7" stroke-width="1"/></svg>
      </div>
      <div class="contact__row">www.orvanelasset.com
        <svg viewBox="0 0 14 14"><path d="M3 1 L3 12 L6 9 L8 13 L10 12 L8 8 L12 8 Z"/></svg>
      </div>
      <div class="contact__rule"></div>
      <div class="contact__row">
        <div class="contact__address">48 Hollis Ave.<br>Newark, NJ 07102</div>
        <svg viewBox="0 0 14 14"><path d="M7 1 C4 1 2.5 3 2.5 5.2 C2.5 8.5 7 13 7 13 C7 13 11.5 8.5 11.5 5.2 C11.5 3 10 1 7 1 Z M7 3.6 A1.7 1.7 0 1 1 7 7 A1.7 1.7 0 1 1 7 3.6 Z"/></svg>
      </div>
      <div class="contact__rule"></div>
    </div>

    <div class="brand">
      <span class="brand__square"></span>
      <span class="brand__name">Orvanel<br>Asset Partners</span>
    </div>
  </section>

</main>
</body>
</html>
```